General Contractors need a new Crisp updated Card Design

We need a new business card design for our company of 25 years based in Toronto call Holvaster Building Inc. : Our goal is to be the leading commercial contractors in Toronto by providing exceptional value to our clients. We work very hard to deliver professional, quality, service in conjunction with consistent price competitiveness to all of our clients on every single project.

Target Market(s)

Design & Build Clients

Industry/Entity Type

Construction Company

Contact Information for Business Card

Address:
18 North Tamlin Glen Road, Unit 57, Marbrook Vale, ON, K7T 2R9
Office: 905-218-5937

Holvasters Logo
Employee Job Description
Employee Cell Phone #
Employee Email
www.holvaster-example.com

Colors

Designer to choose colors to be used in the design.

Requirements
Must have
• Quote Company Saying:
• "Professional. Quality. Service."
Nice to have
• New Crisp up to date look. simple & fresh ( Not to Busy)
Should not have
• NO BLUE PRINTS ON THE BUSINESS CARDS

```html
<!DOCTYPE html>
<html lang="en">
<head>
<meta charset="utf-8">
<title>Holvaster Building Inc. – Business Card</title>
<link href="https://fonts.googleapis.com/css2?family=Roboto:wght@400;500;700&display=swap" rel="stylesheet">
<style>
  :root {
    --backdrop: #e8e5e0;
    --ink: #050505;
    --paper: #ffffff;
    --teal: #006e62;
    --sage: #a3c2b8;
    --light: #f2f2f2;
  }
  * { margin: 0; padding: 0; box-sizing: border-box; }
  html, body { width: 1200px; height: 960px; overflow: hidden; }
  body {
    background: var(--backdrop);
    font-family: "Roboto", Arial, sans-serif;
    position: relative;
  }
  .card {
    position: absolute;
    width: 600px;
    height: 343px;
    box-shadow: 0 3px 8px rgba(0,0,0,0.35);
    overflow: hidden;
  }
  .card--front { left: 314px; top: 113px; background: var(--ink); }
  .card--back { left: 311px; top: 472px; background: var(--sage); }

  .front-shape { position: absolute; inset: 0; }

  .person { position: absolute; left: 36px; top: 48px; }
  .person__name {
    color: var(--teal);
    font-weight: 500;
    font-size: 21px;
    letter-spacing: 0.3px;
  }
  .person__role {
    color: var(--light);
    font-weight: 500;
    font-size: 14.5px;
    margin-top: 3px;
  }
  .address {
    position: absolute; left: 35px; top: 152px;
    color: var(--light);
    font-size: 14px;
    line-height: 19px;
    font-style: normal;
  }
  .contacts {
    position: absolute; left: 35px; top: 216px;
    list-style: none;
    color: var(--light);
    font-size: 14px;
  }
  .contacts li {
    display: flex; align-items: center;
    height: 19.3px;
  }
  .contacts svg { width: 13px; height: 13px; margin-right: 9px; fill: var(--teal); }

  .brand {
    position: absolute;
    display: flex; align-items: center;
    color: var(--teal);
    font-weight: 700;
    white-space: nowrap;
  }
  .brand__mark { background: var(--teal); flex: none; }
  .brand--front { left: 330px; top: 154px; font-size: 21px; }
  .brand--front .brand__mark { width: 26px; height: 26px; margin-right: 10px; }
  .brand--back { left: 0; right: 0; top: 146px; justify-content: center; font-size: 30px; }
  .brand--back .brand__mark { width: 38px; height: 38px; margin-right: 14px; }

  .tagline {
    position: absolute; left: 0; right: 0; top: 285px;
    text-align: center;
    color: var(--paper);
    font-size: 14.5px;
  }
</style>
</head>
<body>
  <section class="card card--front">
    <svg class="front-shape" width="600" height="343" viewBox="0 0 600 343" aria-hidden="true">
      <defs>
        <path id="chevron" d="M432 0 L620 0 L620 343 L432 343 L272 182 Q258 168 272 154 Z"/>
      </defs>
      <use href="#chevron" fill="var(--teal)" transform="translate(-12 0)"/>
      <use href="#chevron" fill="var(--sage)" transform="translate(-9 -9)"/>
      <use href="#chevron" fill="var(--paper)"/>
    </svg>

    <div class="person">
      <h1 class="person__name">DANIEL MARSH</h1>
      <p class="person__role">CEO/FOUNDER</p>
    </div>

    <address class="address">
      18 North Tamlin Glen Road<br>
      Unit 57, Marbrook Vale, ON<br>
      K7T 2R9
    </address>

    <ul class="contacts">
      <li><svg viewBox="0 0 24 24"><path d="M6.6 10.8a15.1 15.1 0 0 0 6.6 6.6l2.2-2.2c.3-.3.7-.4 1-.2 1.1.4 2.3.6 3.6.6.6 0 1 .4 1 1V20c0 .6-.4 1-1 1A17 17 0 0 1 3 4c0-.6.4-1 1-1h3.5c.6 0 1 .4 1 1 0 1.3.2 2.5.6 3.6.1.3 0 .7-.2 1z"/></svg>905-218-5937</li>
      <li><svg viewBox="0 0 24 24"><path d="M7 1h10a2 2 0 0 1 2 2v18a2 2 0 0 1-2 2H7a2 2 0 0 1-2-2V3a2 2 0 0 1 2-2zm0 3v14h10V4zm5 15.5a1 1 0 1 0 0 2 1 1 0 0 0 0-2z"/></svg>905-218-6044</li>
      <li><svg viewBox="0 0 24 24"><path d="M2 5h20v14H2zm2 2v.5l8 5 8-5V7z"/></svg>info@holvaster-example.com</li>
      <li><svg viewBox="0 0 24 24"><path d="M12 2a10 10 0 1 0 0 20 10 10 0 0 0 0-20zm-1 17.9A8 8 0 0 1 4.2 10L9 15v1a2 2 0 0 0 2 2zm6.9-2.5A2 2 0 0 0 16 16h-1v-3a1 1 0 0 0-1-1H8v-2h2a1 1 0 0 0 1-1V7h2a2 2 0 0 0 2-2v-.4a8 8 0 0 1 2.9 12.8z"/></svg>www.holvaster-example.com</li>
    </ul>

    <div class="brand brand--front">
      <span class="brand__mark"></span>
      <span class="brand__name">Holvaster Building Inc.</span>
    </div>
  </section>

  <section class="card card--back">
    <div class="brand brand--back">
      <span class="brand__mark"></span>
      <span class="brand__name">Holvaster Building Inc.</span>
    </div>
    <p class="tagline">Professional. Quality. Service.</p>
  </section>
</body>
</html>
```